Conceptual Model Diagram for Replacing Medication with Behavior to Support Weight Loss Maintenance

Design a figure of a conceptual model that needs to be inserted into a word document for a PSF grant. This conceptual model illustrates how behavioral strategies can replace the regulatory functions lost after AOM discontinuation. The intervention targets three core vulnerabilities—appetite resurgence, metabolic inflexibility, and suboptimal mindstate—through the domains of Food, Physical Activity, and Mind. Sustained weight loss maintenance occurs at the intersection of these domains. The intervention is delivered within a design framework that makes behaviors easier to perform, aligns them with identity, and reinforces them through virtual support and community, ensuring real-world feasibility and long-term adherence.
Target Market(s)
PSF reviewers
Industry/Entity Type
academic
Other font styles liked:
- arial
Requirements
Must have
- see my attached description

```html
<!DOCTYPE html>
<html lang="en">
<head>
<meta charset="utf-8">
<title>Conceptual Model – Weight Loss Maintenance</title>
<link href="https://fonts.googleapis.com/css2?family=Lato:wght@300;400&family=Exo+2:wght@400&family=Montserrat:wght@600&family=Arimo&display=swap" rel="stylesheet">
<style>
  :root {
    --bg: #ffffff;
    --title-grey: #6b6b6b;
    --title-ink: #111111;
    --venn-fill: #e6e6e6;
    --lens-fill: #b3b3b3;
    --box-fill: #a4a4a7;
    --ring-line: #9c9c9c;
    --label-ink: #141414;
    --band-text: #ffffff;
    --band-tip: #bcbcbc;
  }
  html, body {
    margin: 0;
    padding: 0;
    width: 1200px;
    height: 1200px;
    overflow: hidden;
    background: var(--bg);
  }
  .canvas {
    position: relative;
    width: 1200px;
    height: 1200px;
  }
  .model-title {
    position: absolute;
    top: 208px;
    left: 0;
    width: 1200px;
    margin: 0;
    text-align: center;
    font-family: "Lato", Arial, sans-serif;
    font-weight: 300;
    font-size: 36px;
    line-height: 43px;
    color: var(--title-grey);
  }
  .model-title strong {
    font-weight: 400;
    color: var(--title-ink);
  }
  .model-figure {
    position: absolute;
    top: 0;
    left: 0;
  }
  .band-title { font-family: "Exo 2", Arial, sans-serif; font-size: 25px; fill: var(--band-text); }
  .band-detail { font-family: "Exo 2", Arial, sans-serif; font-size: 17px; fill: var(--band-text); }
  .band-tip { fill: var(--band-tip); }
  .domain-label { font-family: "Montserrat", Arial, sans-serif; font-weight: 600; font-size: 14.5px; fill: var(--label-ink); }
  .core-label { font-family: "Montserrat", Arial, sans-serif; font-weight: 600; font-size: 9.5px; fill: #3a3a3a; }
  .vulnerability-box { fill: var(--box-fill); }
  .vulnerability-text { font-family: "Arimo", Arial, sans-serif; font-size: 11.5px; fill: #ffffff; }
  .connector { stroke: #222; stroke-width: 1; fill: none; }
</style>
</head>
<body>
<div class="canvas">
  <h1 class="model-title">Conceptual Model for Replacing Medication with<br>Behavior to Support <strong>WEIGHT LOSS MAINTENANCE</strong></h1>

  <svg class="model-figure" width="1200" height="1200" viewBox="0 0 1200 1200" aria-label="Conceptual model diagram">
    <defs>
      <radialGradient id="halo" cx="601" cy="706" r="420" gradientUnits="userSpaceOnUse">
        <stop offset="0.78" stop-color="#cfcfcf" stop-opacity="0.75"/>
        <stop offset="1" stop-color="#ffffff" stop-opacity="0"/>
      </radialGradient>
      <linearGradient id="grad-easy" x1="380" y1="520" x2="810" y2="500" gradientUnits="userSpaceOnUse">
        <stop offset="0" stop-color="#bdbdbd"/>
        <stop offset="0.55" stop-color="#7a7a7a"/>
        <stop offset="1" stop-color="#3e3e3e"/>
      </linearGradient>
      <linearGradient id="grad-virtual" x1="820" y1="500" x2="500" y2="990" gradientUnits="userSpaceOnUse">
        <stop offset="0" stop-color="#bdbdbd"/>
        <stop offset="0.5" stop-color="#666"/>
        <stop offset="1" stop-color="#333"/>
      </linearGradient>
      <linearGradient id="grad-identity" x1="510" y1="990" x2="380" y2="500" gradientUnits="userSpaceOnUse">
        <stop offset="0" stop-color="#bdbdbd"/>
        <stop offset="0.5" stop-color="#6a6a6a"/>
        <stop offset="1" stop-color="#3a3a3a"/>
      </linearGradient>

      <clipPath id="clip-food"><circle cx="601" cy="647" r="100"/></clipPath>
      <clipPath id="clip-mind"><circle cx="543" cy="761" r="100"/></clipPath>
      <clipPath id="clip-activity"><circle cx="659" cy="761" r="100"/></clipPath>

      <path id="arc-easy-title" d="M408.7,513.7 A272,272 0 0 1 648.2,438.1"/>
      <path id="arc-easy-line1" d="M550.3,418.4 A292,292 0 0 1 824.7,518.3"/>
      <path id="arc-easy-line2" d="M553.8,438.1 A272,272 0 0 1 836.6,570"/>
      <path id="arc-virtual-title" d="M548.7,1002.4 A301,301 0 0 0 883.9,603.1"/>
      <path id="arc-virtual-line1" d="M890.8,716.1 A290,290 0 0 0 787.4,483.9"/>
      <path id="arc-virtual-line2" d="M913.8,716.9 A313,313 0 0 0 802.2,466.2"/>
      <path id="arc-identity-title" d="M347.3,534.9 A306,306 0 0 0 366.6,902.7"/>
      <path id="arc-identity-line1" d="M316.4,766.5 A291,291 0 0 0 525.7,987.1"/>
      <path id="arc-identity-line2" d="M294.8,771.1 A313,313 0 0 0 399.8,945.8"/>
    </defs>

    <!-- framework ring -->
    <circle class="ring-halo" cx="601" cy="706" r="420" fill="url(#halo)"/>
    <circle class="ring-base" cx="601" cy="706" r="339" fill="#ffffff" stroke="#eceef1" stroke-width="4"/>

    <g class="framework-band">
      <path class="band-identity" d="M486.3,1004.8 A320,320 0 0 1 367,487.8 L409.4,527.3 A262,262 0 0 0 507.1,950.6 Z" fill="url(#grad-identity)"/>
      <path class="band-easy" d="M367,487.8 A320,320 0 0 1 831.2,483.7 L789.5,524 A262,262 0 0 0 409.4,527.3 Z" fill="url(#grad-easy)"/>
      <path class="band-virtual" d="M831.2,483.7 A320,320 0 0 1 486.3,1004.8 L507.1,950.6 A262,262 0 0 0 789.5,524 Z" fill="url(#grad-virtual)"/>

      <path class="band-tip" d="M367,487.8 L365.6,535 L409.4,527.3 Z"/>
      <path class="band-tip" d="M831.2,483.7 L784.1,479.9 L789.5,524 Z"/>
      <path class="band-tip" d="M486.3,1004.8 L530.6,988.4 L507.1,950.6 Z"/>
    </g>

    <circle class="inner-field" cx="601" cy="706" r="262" fill="#ffffff"/>
    <circle class="inner-ring" cx="601" cy="706" r="255" fill="none" stroke="var(--ring-line)" stroke-width="5"/>

    <g class="band-labels">
      <text class="band-title"><textPath href="#arc-easy-title" startOffset="28">Make it Easy:</textPath></text>
      <text class="band-detail"><textPath href="#arc-easy-line1" startOffset="31">habits, routines,</textPath></text>
      <text class="band-detail"><textPath href="#arc-easy-line2" startOffset="28">environment, low friction</textPath></text>

      <text class="band-title"><textPath href="#arc-virtual-title" startOffset="21">Virtual Support and Social Connection:</textPath></text>
      <text class="band-detail"><textPath href="#arc-virtual-line1" startOffset="5">accessibility, community,</textPath></text>
      <text class="band-detail"><textPath href="#arc-virtual-line2" startOffset="5">shared accountability</textPath></text>

      <text class="band-title"><textPath href="#arc-identity-title" startOffset="11">Align with Identity:</textPath></text>
      <text class="band-detail"><textPath href="#arc-identity-line1" startOffset="4">self-concept, Sustain ON model,</textPath></text>
      <text class="band-detail"><textPath href="#arc-identity-line2" startOffset="6">internalization</textPath></text>
    </g>

    <!-- domains -->
    <g class="domain-venn">
      <circle cx="601" cy="647" r="100" fill="var(--venn-fill)"/>
      <circle cx="543" cy="761" r="100" fill="var(--venn-fill)"/>
      <circle cx="659" cy="761" r="100" fill="var(--venn-fill)"/>

      <g role="img" aria-label="Meditation icon: food and mind overlap">
        <circle cx="601" cy="647" r="100" fill="var(--lens-fill)" clip-path="url(#clip-mind)"/>
      </g>
      <g role="img" aria-label="Healthy plate icon: food and physical activity overlap">
        <circle cx="601" cy="647" r="100" fill="var(--lens-fill)" clip-path="url(#clip-activity)"/>
      </g>
      <g role="img" aria-label="Walking figure with heart icon: mind and physical activity overlap">
        <circle cx="543" cy="761" r="100" fill="var(--lens-fill)" clip-path="url(#clip-activity)"/>
      </g>

      <g class="venn-dividers" fill="none" stroke="#ffffff" stroke-width="5">
        <circle cx="601" cy="647" r="100" clip-path="url(#clip-mind)"/>
        <circle cx="601" cy="647" r="100" clip-path="url(#clip-activity)"/>
        <circle cx="543" cy="761" r="100" clip-path="url(#clip-food)"/>
        <circle cx="543" cy="761" r="100" clip-path="url(#clip-activity)"/>
        <circle cx="659" cy="761" r="100" clip-path="url(#clip-food)"/>
        <circle cx="659" cy="761" r="100" clip-path="url(#clip-mind)"/>
      </g>

      <circle class="venn-core" cx="602" cy="719" r="53" fill="var(--venn-fill)" stroke="#ffffff" stroke-width="5"/>
      <text class="core-label" text-anchor="middle">
        <tspan x="602" y="711">Sustained</tspan>
        <tspan x="602" y="723.5">Weight Loss</tspan>
        <tspan x="602" y="736">Maintenance</tspan>
      </text>

      <text class="domain-label" x="600" y="614" text-anchor="middle">FOOD</text>
      <text class="domain-label" x="495" y="764" text-anchor="middle">Mind</text>
      <text class="domain-label" text-anchor="middle">
        <tspan x="697" y="757">Physical</tspan>
        <tspan x="697" y="773">Activity</tspan>
      </text>
    </g>

    <!-- vulnerabilities -->
    <g class="vulnerability appetite">
      <rect class="vulnerability-box" x="561" y="470" width="80" height="46" rx="6"/>
      <text class="vulnerability-text" text-anchor="middle"><tspan x="601" y="490">Appetite</tspan><tspan x="601" y="503">Resurgence</tspan></text>
      <circle cx="601" cy="512" r="1.8" fill="#222"/>
      <line class="connector" x1="601" y1="512" x2="601" y2="570"/>
      <path d="M598,568 L601,574 L604,568 Z" fill="#222"/>
    </g>

    <g class="vulnerability mindstate">
      <rect class="vulnerability-box" x="364" y="683" width="80" height="45" rx="6"/>
      <text class="vulnerability-text" text-anchor="middle"><tspan x="404" y="702">Suboptimal</tspan><tspan x="404" y="715">Mindstate</tspan></text>
      <circle cx="404" cy="724" r="1.8" fill="#222"/>
      <path class="connector" d="M404,724 V758 H466"/>
      <path d="M465,755 L471,758 L465,761 Z" fill="#222"/>
    </g>

    <g class="vulnerability metabolic">
      <rect class="vulnerability-box" x="761" y="683" width="80" height="45" rx="6"/>
      <text class="vulnerability-text" text-anchor="middle"><tspan x="801" y="702">Metabolic</tspan><tspan x="801" y="715">Inflexilbility</tspan></text>
      <circle cx="801" cy="724" r="1.8" fill="#222"/>
      <path class="connector" d="M801,724 V758 H744"/>
      <path d="M745,755 L739,758 L745,761 Z" fill="#222"/>
    </g>
  </svg>
</div>
</body>
</html>
```